Business Card Design Project

Business Card
We are rebranding with a new logo
Industry/Entity Type
Business
Contact Information for Business Card
Dennis Marlow +61 427581962 dennis@qovo.com.au P.O. Box 872 Kelvindale QLD 4309
Requirements
Must have
- Logo

```html
<!DOCTYPE html>
<html lang="en">
<head>
<meta charset="utf-8">
<title>Qovo International – Business Card</title>
<link rel="stylesheet" href="https://fonts.googleapis.com/css2?family=Outfit:wght@400;700&display=swap">
<style>
  :root {
    --navy: #003a78;
    --red: #f23c00;
    --orange: #ff6b00;
    --brand-blue: #1583cf;
    --ink: #111111;
    --paper: #ffffff;
    --backdrop: #ffffff;
  }
  * { margin: 0; padding: 0; box-sizing: border-box; }
  html, body {
    width: 1200px;
    height: 1000px;
    overflow: hidden;
    background: var(--backdrop);
    font-family: "Outfit", sans-serif;
  }
  .business-card {
    position: absolute;
    left: 125px;
    top: 210px;
    width: 937px;
    height: 573px;
    background: var(--paper);
    overflow: hidden;
  }
  .artwork-top {
    position: absolute;
    left: 0;
    top: 0;
    width: 937px;
    height: 120px;
  }
  .artwork-bottom {
    position: absolute;
    right: 0;
    bottom: 0;
    width: 320px;
    height: 200px;
  }
  .brand {
    position: absolute;
    left: 38px;
    top: 152px;
    color: var(--brand-blue);
    font-weight: 700;
    line-height: 1;
  }
  .brand-name {
    display: block;
    font-size: 74px;
    letter-spacing: 1px;
  }
  .brand-sub {
    display: block;
    font-size: 18px;
    letter-spacing: 3px;
    margin-top: 16px;
    text-transform: uppercase;
  }
  .holder-name {
    position: absolute;
    left: 37px;
    top: 303px;
    font-size: 34px;
    font-weight: 700;
    color: var(--navy);
    text-transform: uppercase;
    letter-spacing: 0.3px;
  }
  .contact-list {
    position: absolute;
    left: 38px;
    top: 383px;
    list-style: none;
  }
  .contact-item {
    display: flex;
    align-items: center;
    height: 47.5px;
    font-size: 32px;
    color: var(--ink);
  }
  .contact-icon {
    width: 40px;
    height: 40px;
    margin-right: 11px;
    flex: none;
  }
</style>
</head>
<body>
  <main class="business-card">
    <svg class="artwork-top" viewBox="0 0 937 120" preserveAspectRatio="none" role="img" aria-label="Decorative angular artwork in navy, red and orange across the top edge">
      <defs>
        <linearGradient id="topTone" x1="0" y1="0" x2="1" y2="0">
          <stop offset="0" stop-color="var(--navy)"/>
          <stop offset="0.55" stop-color="var(--navy)"/>
          <stop offset="0.8" stop-color="var(--red)"/>
          <stop offset="1" stop-color="var(--orange)"/>
        </linearGradient>
      </defs>
      <rect width="937" height="120" fill="url(#topTone)"/>
    </svg>

    <svg class="artwork-bottom" viewBox="0 0 320 200" preserveAspectRatio="none" role="img" aria-label="Decorative angular artwork in orange, red and navy in the lower right corner">
      <defs>
        <linearGradient id="bottomTone" x1="0" y1="0" x2="1" y2="1">
          <stop offset="0" stop-color="var(--orange)"/>
          <stop offset="0.45" stop-color="var(--red)"/>
          <stop offset="1" stop-color="var(--navy)"/>
        </linearGradient>
      </defs>
      <rect width="320" height="200" fill="url(#bottomTone)"/>
    </svg>

    <div class="brand">
      <span class="brand-name">Qovo</span>
      <span class="brand-sub">International</span>
    </div>

    <h1 class="holder-name">Dennis Marlow</h1>

    <ul class="contact-list">
      <li class="contact-item">
        <svg class="contact-icon" viewBox="0 0 40 40" aria-hidden="true">
          <circle cx="20" cy="20" r="20" fill="var(--navy)"/>
          <path d="M13 10c1-1 2.5-1 3.3 0l2.5 3.3c.7 1 .6 2.2-.3 3l-1.6 1.5c1.2 2.6 3 4.5 5.6 5.8l1.5-1.6c.8-.9 2-1 3-.3l3.3 2.5c1 .8 1 2.3 0 3.3l-1.5 1.5c-1.3 1.3-3.3 1.6-5 .8-5.4-2.5-9.4-6.5-11.9-11.9-.8-1.7-.5-3.7.8-5z" fill="#fff"/>
        </svg>
        +61 427581962
      </li>
      <li class="contact-item">
        <svg class="contact-icon" viewBox="0 0 40 40" aria-hidden="true">
          <circle cx="20" cy="20" r="20" fill="var(--navy)"/>
          <circle cx="20" cy="20" r="4.5" fill="none" stroke="#fff" stroke-width="3"/>
          <path d="M24.5 16v6c0 2 3.5 2.5 4-1 .8-5-3-10-8.5-10a9 9 0 1 0 5 16.5" fill="none" stroke="#fff" stroke-width="3" stroke-linecap="round"/>
        </svg>
        dennis@qovo.com.au
      </li>
      <li class="contact-item">
        <svg class="contact-icon" viewBox="0 0 40 40" aria-hidden="true">
          <circle cx="20" cy="20" r="20" fill="var(--navy)"/>
          <path d="M20 8a8 8 0 0 0-8 8c0 6 8 15 8 15s8-9 8-15a8 8 0 0 0-8-8z" fill="#fff"/>
          <circle cx="20" cy="16" r="3.2" fill="var(--navy)"/>
        </svg>
        P.O. Box 872 Kelvindale QLD 4309
      </li>
    </ul>
  </main>
</body>
</html>
```